Local Mortgage Broker requires DL Flyer

I Require DL sized design for local mortgage broker. Content that will go on the flyer is attached along with the logo.
Looking for a bright & catchy design with that little OOMPH.....on the creative side.
Am looking for a responsive campaign with this style of marketing. The main message is that "We may be able to save thousands of dollars for you, just give us a chance to review your mortgages"

Target Market(s)

All home owners with a mortgage or eople looking to buy their first home.

Industry/Entity Type

Marketing

```html
<!DOCTYPE html>
<html lang="en">
<head>
<meta charset="utf-8">
<title>KeyWay Lending – DL Flyer</title>
<link rel="stylesheet" href="https://fonts.googleapis.com/css2?family=Open+Sans:wght@400;600;700;800&display=swap">
<style>
  :root {
    --navy: #2a2a6e;
    --navy-deep: #222260;
    --yellow: #f4ec1c;
    --white: #ffffff;
    --stage: #e8e8ea;
    --photo-light: #d9dadf;
    --photo-warm: #c9a08c;
    --photo-red: #d4532e;
  }
  * { box-sizing: border-box; margin: 0; padding: 0; }
  html, body {
    width: 1200px; height: 800px; overflow: hidden;
    background: var(--stage);
    font-family: "Open Sans", Arial, sans-serif;
  }
  .canvas {
    width: 1200px; height: 800px;
    display: flex; justify-content: center; align-items: center; gap: 80px;
  }
  .flyer {
    position: relative;
    width: 330px; height: 700px;
    background: var(--navy);
    overflow: hidden;
    box-shadow: 0 6px 18px rgba(0,0,0,0.18);
  }
  .flyer__header {
    height: 72px;
    display: flex; align-items: center; justify-content: center;
    text-align: center;
    color: var(--yellow);
    font-weight: 800; font-size: 19px; line-height: 1.15;
    letter-spacing: 0.3px;
    background: var(--navy);
  }
  .flyer__photo {
    height: 180px;
    background:
      radial-gradient(ellipse 90px 60px at 48% 42%, var(--photo-red) 0%, rgba(212,83,46,0.5) 45%, transparent 75%),
      radial-gradient(ellipse 140px 110px at 40% 75%, var(--photo-warm) 0%, transparent 80%),
      linear-gradient(160deg, var(--photo-light), #eeeeef 60%, #c8c9cf);
  }
  .brand-tile {
    position: absolute; right: 0; top: 196px;
    width: 140px; height: 56px;
    background: var(--white);
    display: flex; align-items: center; justify-content: center; gap: 7px;
    color: var(--navy);
    font-weight: 800; font-size: 14px;
  }
  .brand-tile__mark {
    width: 12px; height: 12px; background: var(--navy);
  }
  .photo-caption {
    position: absolute; left: 12px; top: 212px;
    width: 128px; padding: 6px 8px;
    background: var(--navy);
    color: var(--white);
    font-size: 8.5px; font-weight: 700; line-height: 1.3;
    text-align: center;
  }
  .flyer__body {
    padding: 22px 22px 0;
    text-align: center;
    color: var(--white);
  }
  .offer__amount { font-size: 40px; font-weight: 800; line-height: 1; }
  .offer__terms { font-size: 14px; font-weight: 700; margin-top: 6px; }
  .offer__pitch { font-size: 20px; font-weight: 800; line-height: 1.15; margin-top: 14px; }
  .cta { color: var(--yellow); font-weight: 800; }
  .cta--front { font-size: 24px; line-height: 1.2; margin-top: 24px; }
  .cta--front .cta__phone { font-size: 29px; display: block; }
  .web { font-size: 15px; font-weight: 700; margin-top: 18px; }
  .footnote {
    font-size: 9px; line-height: 1.45; margin-top: 22px; font-weight: 400;
  }
  .copy { font-size: 10px; line-height: 1.5; text-align: left; }
  .benefits {
    list-style: none; text-align: left; margin: 14px 0;
    color: var(--yellow); font-size: 10.5px; font-weight: 700; line-height: 1.55;
  }
  .benefits li::before { content: "•"; margin-right: 6px; }
  .cta--back { font-size: 19px; line-height: 1.3; margin-top: 22px; }
  .flyer__strip {
    position: absolute; left: 0; right: 0; bottom: 0;
    height: 16px; background: var(--yellow);
  }
  .flyer--back .flyer__body { padding-top: 26px; }
  .flyer--back .web { margin-top: 20px; }
</style>
</head>
<body>
<main class="canvas">

  <article class="flyer flyer--front">
    <header class="flyer__header">FIND THE RIGHT<br>FINANCE SOLUTION</header>
    <div class="flyer__photo" role="img" aria-label="Photo of hands holding a small model house with a red roof"></div>
    <div class="brand-tile"><span class="brand-tile__mark"></span>KeyWay Lending</div>
    <p class="photo-caption">Get up to $3000 voucher or cash back* on the settlement of your loan.</p>
    <section class="flyer__body">
      <p class="offer__amount">UP TO $3000</p>
      <p class="offer__terms">*CONDITIONS APPLY</p>
      <p class="offer__pitch">GET REWARDED BY<br>SWITCHING OVER</p>
      <p class="cta cta--front">Call us on <span class="cta__phone">0400 555 018</span></p>
      <p class="web">www.keywaylending.com.au</p>
      <p class="footnote">*based on the size of the loan, you get up to 0.3% of your total loan settled through us. For example a refinance of $600,000 mortgage to any of our panel lenders will get you 0.30% of the $600,000, which is $1,800 as your bonus/reward.</p>
    </section>
    <div class="flyer__strip"></div>
  </article>

  <article class="flyer flyer--back">
    <header class="flyer__header">FIND THE RIGHT<br>FINANCE SOLUTION</header>
    <div class="flyer__photo" role="img" aria-label="Photo of hands holding a small model house with a red roof"></div>
    <div class="brand-tile"><span class="brand-tile__mark"></span>KeyWay Lending</div>
    <p class="photo-caption">The right loan to suit your individual requirements.</p>
    <section class="flyer__body">
      <p class="copy">Whether you are looking to buy your first home, renovate, refinance or invest, we're here to negotiate the right finance for you. We're a one-stop shop with hundreds of loan options available from across Australia's leading lenders and we'll work with you to find the right finance solution to meet your needs.</p>
      <ul class="benefits">
        <li>Refinance existing Mortgage</li>
        <li>Purchase First Home</li>
        <li>Purchase Investment Property</li>
        <li>Upgrade or Renovate existing Property</li>
      </ul>
      <p class="copy">We are confident that we may be able to save you thousands of dollars over the term of your loan by simply reviewing your existing home loan.</p>
      <p class="cta cta--back">Call us on 0400 555 018<br>To find out how!</p>
      <p class="web">www.keywaylending.com.au</p>
    </section>
    <div class="flyer__strip"></div>
  </article>

</main>
</body>
</html>
```